Freelance business trainer needs a new business card

My business is called Tbrite. I provide training in the workplace on management, coaching and mentoring, and customer service topics for a variety of businesses, colleges and private training providers, and teach on management programs. I need a professional but eye catching business card. Business colours grey and orange. My name Linda Marchbank; Tel 07853 416207; email lmarchbank@tbrite.co.uk; website www.tbrite.co.uk.
Happy to have some sort of logo on front and details on back or all on one side
Target Market(s)
SME businesses and colleges - workshops i run are for adults in the workplace
Industry/Entity Type
Training
Look and feel

```html
<!DOCTYPE html>
<html lang="en">
<head>
<meta charset="utf-8">
<title>Tbrite – Business Card</title>
<link rel="stylesheet" href="https://fonts.googleapis.com/css2?family=Open+Sans:wght@400;600;700&display=swap">
<style>
  :root {
    --stage: #5c5c5c;
    --card: #414141;
    --band: #5a5a5a;
    --orange: #f7931e;
    --white: #ffffff;
    --text-light: #f2f2f2;
  }
  * { box-sizing: border-box; margin: 0; padding: 0; }
  html, body {
    width: 1200px;
    height: 750px;
    overflow: hidden;
    background: var(--stage);
    font-family: "Open Sans", sans-serif;
  }
  .canvas {
    position: relative;
    width: 1200px;
    height: 750px;
  }
  .card {
    position: absolute;
    top: 215px;
    width: 497px;
    height: 286px;
    border-radius: 16px;
    background: var(--card);
    overflow: hidden;
  }
  .card--front { left: 88px; }
  .card--back { left: 617px; }

  /* Brand name */
  .brand {
    display: flex;
    align-items: center;
    gap: 12px;
    color: var(--orange);
    font-weight: 600;
    line-height: 1;
  }
  .brand__square {
    background: var(--orange);
    flex: none;
  }

  /* Front */
  .card--front .brand {
    position: absolute;
    left: 0; right: 0;
    top: 92px;
    justify-content: center;
    font-size: 68px;
  }
  .card--front .brand__square { width: 46px; height: 46px; }
  .web-band {
    position: absolute;
    left: 0; right: 0;
    top: 245px;
    height: 26px;
    background: var(--band);
    color: var(--text-light);
    font-size: 15px;
    letter-spacing: 1.5px;
    text-align: center;
    line-height: 26px;
  }

  /* Back */
  .card--back .brand {
    position: absolute;
    left: 48px;
    top: 48px;
    font-size: 54px;
    gap: 10px;
  }
  .card--back .brand__square { width: 38px; height: 38px; }
  .side-panel {
    position: absolute;
    top: 0;
    right: 0;
    width: 160px;
    height: 100%;
    background: var(--orange);
  }
  .holder {
    position: absolute;
    right: 12px;
    top: 52px;
    text-align: right;
    color: var(--white);
    line-height: 1.35;
  }
  .holder__name { font-size: 14px; font-weight: 700; }
  .holder__role { font-size: 14px; font-weight: 400; }
  .contacts {
    position: absolute;
    left: 46px;
    top: 186px;
    list-style: none;
    color: var(--text-light);
    font-size: 15px;
  }
  .contacts__item {
    display: flex;
    align-items: center;
    gap: 8px;
    height: 21.5px;
  }
  .contacts__icon { width: 13px; height: 13px; flex: none; }
</style>
</head>
<body>
<main class="canvas">

  <section class="card card--front" aria-label="Business card front">
    <div class="brand"><span class="brand__square"></span>Tbrite</div>
    <div class="web-band">www.tbrite.co.uk.</div>
  </section>

  <section class="card card--back" aria-label="Business card back">
    <div class="side-panel"></div>

    <div class="brand"><span class="brand__square"></span>Tbrite</div>

    <div class="holder">
      <p class="holder__name">Linda Marchbank</p>
      <p class="holder__role">Owner</p>
    </div>

    <ul class="contacts">
      <li class="contacts__item">
        <svg class="contacts__icon" viewBox="0 0 16 16" aria-hidden="true">
          <path d="M2 6 C2 3 5 2 8 2 C11 2 14 3 14 6 L11 6 L10 4.5 L6 4.5 L5 6 Z" fill="var(--orange)"/>
          <rect x="3" y="7" width="10" height="7" rx="1.5" fill="var(--orange)"/>
          <circle cx="8" cy="10.5" r="1.8" fill="var(--card)"/>
        </svg>
        07853 416207
      </li>
      <li class="contacts__item">
        <svg class="contacts__icon" viewBox="0 0 16 16" aria-hidden="true">
          <rect x="1" y="3" width="14" height="10" rx="1" fill="var(--orange)"/>
          <path d="M1.5 3.5 L8 9 L14.5 3.5" fill="none" stroke="var(--card)" stroke-width="1.3"/>
        </svg>
        lmarchbank@tbrite.co.uk
      </li>
      <li class="contacts__item">
        <svg class="contacts__icon" viewBox="0 0 16 16" aria-hidden="true">
          <circle cx="8" cy="8" r="7" fill="var(--orange)"/>
          <g fill="none" stroke="var(--card)" stroke-width="1">
            <ellipse cx="8" cy="8" rx="3" ry="7"/>
            <line x1="1" y1="8" x2="15" y2="8"/>
            <line x1="2.2" y1="4.5" x2="13.8" y2="4.5"/>
            <line x1="2.2" y1="11.5" x2="13.8" y2="11.5"/>
          </g>
        </svg>
        www.tbrite.co.uk.
      </li>
    </ul>
  </section>

</main>
</body>
</html>
```